Create a banner for me that embodies my health and well being package.

I am an intuitive counselor with a busy practice helping clients to shift their blocks and move forward in their lives.
I have created a package called '9 paths home again'
I am wanting a banner to put on my website page, facebook page and to use as a letter head in mailouts.
My ideal clients are those who want to create change in their lives and who invest money in themselves and their personal and spiritual growth.
I am different to regular life coaches as my sessions have a spiritual twist to them creating much deeper change in my clients.
I would like the banner to be mainly font with the title of the progam: 9 Paths Home Again (no other wording) (something along the lines of the Blackjack font) and that ties in with the theme of my website. I'm not sure what else I want with it and am looking for ideas.
Website:
www.quillorabalancecare.com.au
I also have a current facebook page for the business:
https://www.facebook.com/Quillora-Balance-Care-402715938846102/
(Note: I am about to drop my logo and business name and move to using my own name - the rest of the website will remain the same).
I have attached a doc with the draft of what wording will be on the website page any advertising will link to, to give you an idea of what the program is about.

Target Market(s)

People who invest money on themselves who are looking to improve their emotional well being and creating change in their life. Majority are middle aged women (also younger females and some men)

Industry/Entity Type

Health And Wellness

Font styles to use
Other font styles liked:
• I like Blackjack and Amienne. Along those lines.

Requirements
Must have
• Attractive, modern and GREAT font.
Nice to have
• Surprise me with something amazing!
• I love the colours in the 2 images I have up loaded as they represent the heart chakra colours. They could be a feature on the banner or blurred into the background.
Should not have
• Even though my work is quite spiritual I don't want it to look woo woo (meaning airy fairy spiritual stuff!)

```html
<!DOCTYPE html>
<html lang="en">
<head>
<meta charset="utf-8">
<title>9 Paths Home Again – Cover Banner</title>
<link rel="stylesheet" href="https://fonts.googleapis.com/css2?family=Arimo:wght@400;700&family=Caveat:wght@500&display=swap">
<style>
  :root {
    --forest-deep: #1f3438;
    --forest-mid: #46676a;
    --mist: #b3c6c4;
    --grass: #6b5b48;
    --title-ink: #f6f6f1;
    --name-ink: #ffffff;
    --frame: #2b1d22;
    --lotus-pink: #d2558e;
    --lotus-leaf: #6f9a6a;
    --lotus-sky: #a8c9d6;
    --button-bg: #f6f7f9;
    --button-border: #ced0d4;
    --button-ink: #4b4f56;
    --page-bg: #ffffff;
  }
  html, body {
    margin: 0;
    padding: 0;
    width: 1200px;
    height: 444px;
    overflow: hidden;
    background: var(--page-bg);
  }
  .cover-banner {
    position: relative;
    width: 1200px;
    height: 444px;
    overflow: hidden;
  }
  .forest-photo {
    position: absolute;
    inset: 0;
    background:
      radial-gradient(ellipse 30% 55% at 55% 40%, rgba(200,214,211,0.8), rgba(200,214,211,0) 70%),
      linear-gradient(to bottom, rgba(0,0,0,0) 60%, var(--grass) 100%),
      linear-gradient(to right, var(--forest-deep) 0%, var(--forest-mid) 22%, var(--mist) 48%, var(--mist) 58%, var(--forest-mid) 80%, var(--forest-deep) 100%);
  }
  .program-title {
    position: absolute;
    left: 555px;
    top: 176px;
    width: 200px;
    margin: 0;
    font-family: "Caveat", cursive;
    font-weight: 500;
    font-size: 62px;
    line-height: 63px;
    color: var(--title-ink);
    text-align: center;
    text-shadow: 0 1px 3px rgba(0,0,0,0.4);
  }
  .program-title span { display: block; }
  .profile-frame {
    position: absolute;
    left: 24px;
    top: 243px;
    width: 244px;
    height: 230px;
    background: var(--frame);
  }
  .profile-photo {
    position: absolute;
    left: 25px;
    top: 22px;
    width: 193px;
    height: 200px;
    background:
      radial-gradient(ellipse 45% 40% at 50% 55%, var(--lotus-pink), rgba(210,85,142,0) 75%),
      linear-gradient(to bottom, var(--lotus-sky) 0%, #d9e6e9 45%, var(--lotus-leaf) 100%);
  }
  .page-identity {
    position: absolute;
    left: 292px;
    top: 282px;
    font-family: "Arimo", Arial, sans-serif;
    color: var(--name-ink);
    text-shadow: 0 1px 3px rgba(0,0,0,0.55);
  }
  .page-name {
    margin: 0;
    font-size: 28px;
    font-weight: 400;
    line-height: 33px;
  }
  .page-category {
    margin: 14px 0 0;
    font-size: 22px;
    line-height: 26px;
  }
  .page-actions {
    position: absolute;
    top: 393px;
    left: 723px;
    display: flex;
    font-family: "Arimo", Arial, sans-serif;
  }
  .action-button {
    display: flex;
    align-items: center;
    gap: 8px;
    height: 37px;
    padding: 0 14px;
    box-sizing: border-box;
    background: var(--button-bg);
    border: 1px solid var(--button-border);
    border-radius: 3px;
    color: var(--button-ink);
    font-size: 17px;
    font-weight: 700;
  }
  .action-donate { width: 154px; margin-right: 14px; }
  .action-like { width: 88px; margin-right: 14px; }
  .action-message { width: 122px; border-radius: 3px 0 0 3px; }
  .action-more { width: 76px; justify-content: center; border-left: none; border-radius: 0 3px 3px 0; margin-left: 2px; }
  .action-icon { width: 18px; height: 18px; fill: var(--button-ink); flex: none; }
</style>
</head>
<body>
  <main class="cover-banner">
    <div class="forest-photo" role="img" aria-label="Misty bamboo forest with a woman in silhouette standing with arms spread wide, a faint mandala pattern behind her"></div>
    <h1 class="program-title">
      <span>9 Paths</span>
      <span>Home</span>
      <span>Again</span>
    </h1>
    <div class="profile-frame">
      <div class="profile-photo" role="img" aria-label="Pink lotus flower in bloom against a soft blue and green background"></div>
    </div>
    <div class="page-identity">
      <p class="page-name">Quillora<br>Balance Care</p>
      <p class="page-category">Medical and Health</p>
    </div>
    <div class="page-actions">
      <div class="action-button action-donate">
        <svg class="action-icon" viewBox="0 0 20 20" aria-hidden="true"><path d="M10 18 2.5 10.5A4.5 4.5 0 0 1 10 4.2a4.5 4.5 0 0 1 7.5 6.3z"/></svg>
        Donate Now
      </div>
      <div class="action-button action-like">
        <svg class="action-icon" viewBox="0 0 20 20" aria-hidden="true"><circle cx="10" cy="10" r="6"/></svg>
        Like
      </div>
      <div class="action-button action-message">
        <svg class="action-icon" viewBox="0 0 20 20" aria-hidden="true"><path d="M2 3h16v11H8l-4 4v-4H2z"/></svg>
        Message
      </div>
      <div class="action-button action-more">
        <svg width="26" height="6" viewBox="0 0 26 6" aria-hidden="true" fill="#4b4f56"><circle cx="3" cy="3" r="2.6"/><circle cx="13" cy="3" r="2.6"/><circle cx="23" cy="3" r="2.6"/></svg>
      </div>
    </div>
  </main>
</body>
</html>
```